Book Cover Design Project

I am wanting a book cover for an free downloadable e-book called "The 5 Quiet Leaks that will Sink your Venture"
KPW are chartered accountants based in Wellington NZ, working with SME's and owener-managed businesses who want to grow their business further.
Purpose:
Ultimately to get NZ-based business owners to give us their email addresses so that we can market to them.
To be promoted via our communications with clients and into the databases of strategic partners, as well as using google ads to promote more widely.
Target market:
Owners of businesses that are hitting the $1M (or so) turnover mark and who want to grow further. But they are finding that their business has reaching a level of complexity that requires them to start thinking about it differently, and requiring them to get off the tools and out of the way of the growing and developing team. Chances are, they have been in charge of everything that happens in the business thus far and are now working harder than the ever expected to and work/life balance has gone out the window.
KPW Brand Promise:
We talk your language.
KPW Goal:
To change the world’s view of accountants. By that we mean that we do not want to conform to the stereotype, and that our approach will be professional, but not too serious.

```html
<!DOCTYPE html>
<html lang="en">
<head>
<meta charset="utf-8">
<title>The 5 Quiet Leaks that will Sink your Venture</title>
<link rel="stylesheet" href="https://fonts.googleapis.com/css2?family=Anton&display=swap">
<style>
  :root {
    --cover-dark: #5f5f5f;
    --numeral-orange: #fb9a36;
    --target-red: #d40d0d;
    --title-maroon: #98123a;
    --subtitle-navy: #2e3182;
    --subtitle-white: #ffffff;
    --brand-plate: #ffffff;
    --brand-orange: #f07a1a;
  }
  html, body {
    margin: 0;
    padding: 0;
    width: 900px;
    height: 1200px;
    overflow: hidden;
    background: var(--cover-dark);
  }
  .cover {
    display: block;
    width: 900px;
    height: 1200px;
  }
  .numeral {
    font-family: "Anton", "Arial Narrow", sans-serif;
    fill: var(--numeral-orange);
  }
  .title {
    font-family: "Anton", "Arial Narrow", sans-serif;
    fill: var(--title-maroon);
  }
  .subtitle {
    font-family: "Anton", "Arial Narrow", sans-serif;
  }
  .subtitle .navy { fill: var(--subtitle-navy); }
  .subtitle .white { fill: var(--subtitle-white); }
  .brand-name {
    font-family: "Anton", "Arial Narrow", sans-serif;
    fill: var(--brand-orange);
    letter-spacing: 1px;
  }
</style>
</head>
<body>
<svg class="cover" viewBox="0 0 900 1200" xmlns="http://www.w3.org/2000/svg" aria-labelledby="cover-title">
  <title id="cover-title">The 5 Quiet Leaks that will Sink your Venture</title>
  <defs>
    <linearGradient id="cover-base" x1="0" y1="0" x2="0" y2="1">
      <stop offset="0" stop-color="#6c6c6c"/>
      <stop offset="1" stop-color="#5a5a5a"/>
    </linearGradient>
    <linearGradient id="cover-swoosh" x1="0" y1="0" x2="1" y2="1">
      <stop offset="0" stop-color="#9a9a9a"/>
      <stop offset="0.55" stop-color="#bdbdbd"/>
      <stop offset="1" stop-color="#d6d6d6"/>
    </linearGradient>
    <radialGradient id="target-tone" cx="0.5" cy="0.5" r="0.5">
      <stop offset="0" stop-color="#d40d0d" stop-opacity="0.25"/>
      <stop offset="0.8" stop-color="#d40d0d" stop-opacity="0.55"/>
      <stop offset="1" stop-color="#d40d0d" stop-opacity="0.8"/>
    </radialGradient>
  </defs>

  <!-- background -->
  <rect class="cover-base" width="900" height="1200" fill="url(#cover-base)"/>
  <path class="cover-swoosh"
        d="M0 0 H900 V1060 C860 900 760 760 560 660 C360 560 160 420 30 40 L0 40 Z"
        fill="url(#cover-swoosh)" opacity="0.85"/>
  <path class="cover-top-band" d="M0 0 H900 V60 C600 20 300 30 0 60 Z" fill="#7a7a7a" opacity="0.6"/>

  <!-- large numeral -->
  <text class="numeral" x="125" y="965" font-size="890" transform="skewX(-8)" transform-origin="380 600">5</text>

  <!-- target artwork area -->
  <circle class="target-art" cx="590" cy="275" r="190" fill="url(#target-tone)"
          role="img" aria-label="Red crosshair target graphic"/>

  <!-- title -->
  <text class="title" x="112" y="762" font-size="112" textLength="690" lengthAdjust="spacingAndGlyphs">Quiet Leaks</text>
  <text class="subtitle" x="65" y="857" font-size="70" textLength="755" lengthAdjust="spacingAndGlyphs"><tspan class="navy">that will </tspan><tspan class="white">Sink</tspan><tspan class="navy"> your </tspan><tspan class="white">Venture</tspan></text>

  <!-- brand plate -->
  <rect class="brand-plate" x="30" y="1015" width="420" height="58" fill="var(--brand-plate)"/>
  <text class="brand-name" x="52" y="1056" font-size="28">kerr paton wynn ltd</text>
</svg>
</body>
</html>
```